Kestrel Plumbing business card full re design & logo design

Kestrel Plumbing is a Sydney based mechanical plumbing contractor company.
We would like a full redesign with new logo etc which we can take to a future website, uniforms, vehicle sign writing etc.
Blue is my preferred choice of colour but i would be open to see a couple of alternatives thrown in the mix to see how they compare. I am open to see on white cards, black cards etc. Open to many new ideas.
Please see attached original business cards which have been used for the last 5 years.

Target Market(s)

Mechanical services industry.

Industry/Entity Type

Plumbing

Contact Information for Business Card

Dale Fenmore
Director

Mob: 0427 596 418
Email: dale@kestrelplumbing-demo.net.au
PO BOX 782
Harrowdale NSW 2199
Lic: 518604k

Logo Text

Kestrel Plumbing

Font styles to use
Sans Serif

Colors
0655a3
3276b5
0792cd
33a6d7
85cae6
000000
333333
474747

Requirements
Must have
• Things that make it very professional and very well presented.
Nice to have
• Same description or very similar to attached uploaded file
Should not have
• Anything that makes it look unprofessional or cartoony.

```html
<!DOCTYPE html>
<html lang="en">
<head>
<meta charset="utf-8">
<title>Kestrel Plumbing – Business Card</title>
<link rel="stylesheet" href="https://fonts.googleapis.com/css2?family=Open+Sans:ital,wght@0,400;0,600;0,700;0,800;1,800&display=swap">
<style>
  :root {
    --blue-deep: #0655a3;
    --blue-mid: #3276b5;
    --blue-bright: #0792cd;
    --blue-sky: #33a6d7;
    --blue-pale: #85cae6;
    --black: #000000;
    --grey-dark: #333333;
    --grey: #474747;
    --white: #ffffff;
    --stage: #2b2b2b;
  }
  * { box-sizing: border-box; margin: 0; padding: 0; }
  html, body { width: 1200px; height: 880px; overflow: hidden; }
  body {
    background: var(--stage);
    font-family: "Open Sans", Arial, sans-serif;
    position: relative;
  }
  .card {
    position: absolute;
    width: 660px;
    height: 402px;
    border-radius: 22px;
    overflow: hidden;
    background: linear-gradient(135deg, #1a63b8 0%, var(--blue-deep) 70%);
    color: var(--white);
  }
  .card--front { left: 40px; top: 30px; }
  .card--back { left: 500px; top: 448px; }

  /* front */
  .front-panel { position: absolute; right: 0; top: 0; width: 300px; height: 340px; }
  .wordmark { position: absolute; font-weight: 800; color: var(--white); line-height: 1; letter-spacing: 3px; text-transform: uppercase; }
  .wordmark__top { display: block; font-size: 40px; }
  .wordmark__bottom { display: block; font-size: 20px; letter-spacing: 12px; margin-top: 6px; }
  .card--front .wordmark { left: 48px; top: 60px; }
  .contact { position: absolute; left: 78px; top: 168px; font-size: 15px; line-height: 1.3; }
  .contact__name { font-weight: 700; font-size: 21px; }
  .contact__role { font-size: 14px; margin-bottom: 18px; }
  .contact__row { display: flex; align-items: center; gap: 8px; }
  .contact__row svg { width: 15px; height: 15px; flex: none; }

  .band {
    position: absolute; left: 0; right: 0; bottom: 0; height: 58px;
    background: var(--black);
    border-top: 3px solid var(--blue-sky);
    display: flex; align-items: center;
    font-weight: 800; text-transform: uppercase; letter-spacing: 1px;
  }
  .card--front .band { padding-left: 78px; font-size: 16px; word-spacing: 3px; }

  /* back */
  .brand-lockup { position: absolute; left: 40px; top: 46px; display: flex; align-items: center; gap: 22px; }
  .brand-lockup__dot { width: 74px; height: 74px; border-radius: 50%; border: 8px solid var(--white); }
  .brand-lockup__rule { width: 2px; height: 100px; background: var(--white); }
  .brand-lockup .wordmark { position: static; }
  .services-title { position: absolute; left: 40px; top: 180px; font-size: 22px; font-weight: 800; text-transform: uppercase; }
  .specialties-label { position: absolute; left: 40px; top: 218px; font-size: 21px; font-weight: 700; }
  .specialties { position: absolute; list-style: none; font-size: 16px; line-height: 1.35; }
  .specialties--a { left: 40px; top: 256px; }
  .specialties--b { left: 290px; top: 256px; }
  .specialties li { display: flex; align-items: center; gap: 10px; }
  .specialties li::before { content: ""; width: 9px; height: 9px; border-radius: 50% 0 50% 50%; transform: rotate(-45deg); background: var(--black); }
  .card--back .band {
    height: 50px;
    background: linear-gradient(90deg, var(--black) 55%, rgba(0,0,0,0) 100%);
    padding-left: 40px; font-size: 19px; letter-spacing: 2px;
  }
  .band__lower { text-transform: none; font-style: italic; }
</style>
</head>
<body>

<section class="card card--front" aria-label="Business card front">
  <svg class="front-panel" viewBox="0 0 300 340" aria-hidden="true">
    <path d="M300 0 H80 C30 90 30 230 110 340 H300 Z" fill="#ffffff"/>
  </svg>
  <div class="wordmark">
    <span class="wordmark__top">Kestrel</span>
    <span class="wordmark__bottom">Plumbing</span>
  </div>
  <div class="contact">
    <p class="contact__name">Dale Fenmore</p>
    <p class="contact__role">Director</p>
    <p>PO BOX 782</p>
    <p>Harrowdale NSW 2199</p>
    <p class="contact__row">
      <svg viewBox="0 0 16 16" aria-hidden="true"><rect x="1" y="1" width="14" height="14" fill="#000"/><rect x="4" y="3" width="8" height="10" rx="1" fill="none" stroke="#fff" stroke-width="1.5"/></svg>
      0427 596 418
    </p>
    <p class="contact__row">
      <svg viewBox="0 0 16 16" aria-hidden="true"><rect x="1" y="1" width="14" height="14" fill="#000"/><path d="M3 5 H13 V11 H3 Z M3 5 L8 9 L13 5" fill="none" stroke="#fff" stroke-width="1.2"/></svg>
      dale@kestrelplumbing-demo.net.au
    </p>
  </div>
  <div class="band">Mechanical Piping | CHW | HW | CW | Refrig</div>
</section>

<section class="card card--back" aria-label="Business card back">
  <div class="brand-lockup">
    <span class="brand-lockup__dot" aria-hidden="true"></span>
    <span class="brand-lockup__rule" aria-hidden="true"></span>
    <div class="wordmark">
      <span class="wordmark__top">Kestrel</span>
      <span class="wordmark__bottom">Plumbing</span>
    </div>
  </div>
  <h2 class="services-title">Mechanical Plumbing Services</h2>
  <p class="specialties-label">Specialising in:</p>
  <ul class="specialties specialties--a">
    <li>Make Good</li>
    <li>Refurbishment</li>
    <li>Tenancy Fit Out</li>
  </ul>
  <ul class="specialties specialties--b">
    <li>Plant Room Works</li>
    <li>Shut Downs</li>
    <li>Change Overs</li>
  </ul>
  <div class="band">Kestrel&nbsp;<span class="band__lower">have the</span>&nbsp;Solution</div>
</section>

</body>
</html>
```